Webdesign für Dentallabor
Zielgruppe
Wir sind ein Dentallabor. Unsere Zielgruppe sind Zahnarztpraxen, keine Privatpersonen. Dementsprechend soll die Website informativ und anschaulich gestaltet sein.
Aufgabenstellung
Die Website soll schlicht in den Farben blau, dunkelblau und weiß (wie die Farben des Logos) gehalten sein. Es sollen Stock-Fotos verwendet werden, die die Leistungen des Dentallabors zeigen und zu dem Thema passen.
Es soll eine Onepage-Website werden, die so aufgebaut ist, wie die Website unter dem folgenden Link: https://www.klar-und-fest-gebaut.de/

```html
<!DOCTYPE html>
<html lang="de">
<head>
<meta charset="utf-8">
<title>Lindholt Dentallabor</title>
<link href="https://fonts.googleapis.com/css2?family=Exo+2:wght@700;800&family=Montserrat:wght@400;500;600;700&display=swap" rel="stylesheet">
<style>
:root{
  --navy:#1c2e4f;
  --blue:#4a80c6;
  --blue-soft:#c6d4e6;
  --text:#2b3445;
  --white:#ffffff;
  --footer:#3d5f8f;
  --rule:#b4b8bf;
}
*{margin:0;padding:0;box-sizing:border-box}
html,body{width:1200px;height:3125px;overflow:hidden;background:var(--white)}
body{font-family:'Montserrat',sans-serif;color:var(--text)}
.page{position:relative;width:1200px;height:3125px;overflow:hidden}
.abs{position:absolute}
.display{font-family:'Exo 2',sans-serif;font-weight:800;color:var(--navy)}

.hero-bg{left:0;top:0;width:1200px;height:688px;
  background:radial-gradient(ellipse 420px 620px at 600px 260px,#ffffff 35%,rgba(255,255,255,0) 100%),linear-gradient(180deg,#e6edf5 0%,#c4d3e6 100%)}
.hero-photo{left:352px;top:400px;width:497px;height:377px;border-radius:40% 40% 45% 45%;
  background:radial-gradient(ellipse at center,#e9e6e0 0%,#eef0f3 55%,rgba(255,255,255,0) 78%)}
.topbar{left:159px;top:26px;display:flex;gap:22px;font-size:13.5px;color:var(--navy)}
.topbar span{display:flex;align-items:center;gap:7px}
.brand{left:900px;top:52px;width:140px;text-align:right;font-weight:700;font-size:19px;color:var(--blue);display:flex;align-items:center;justify-content:flex-end;gap:8px}
.brand i{display:block;width:16px;height:16px;background:var(--blue)}
.hero-title{left:340px;top:160px;width:520px;text-align:center;font-size:23px;line-height:28px}
.hero-text{left:385px;top:274px;width:430px;text-align:center;font-size:13px;line-height:19.5px}
.btn{top:364px;height:37px;border:2px solid var(--blue);display:flex;align-items:center;justify-content:center;font-size:13px;color:var(--navy);background:rgba(255,255,255,.35)}
.btn-a{left:432px;width:190px;border-width:1.5px;color:#4a5568}
.btn-b{left:638px;width:127px}

.sec-title{left:0;width:1200px;text-align:center;font-size:24px}
.sec-rule{left:580px;width:57px;height:2px;background:var(--navy)}
.sec-sub{left:0;width:1200px;text-align:center;font-size:19.5px;color:var(--blue);font-weight:500}
.about-text{left:383px;width:434px;text-align:center;font-size:10.6px;line-height:16.2px}
.about-text b{font-weight:700;color:var(--navy)}
.photo-lab{left:312px;top:1116px;width:446px;height:296px;background:linear-gradient(120deg,#e9e9e9,#cfc8c0 50%,#f1f1f1)}
.services-bg{left:0;top:1483px;width:1200px;height:1010px;background:linear-gradient(180deg,#c6d4e6 0%,#e3eaf3 60%,#ffffff 100%)}
.photo-implant{left:607px;top:1315px;width:331px;height:230px;background:linear-gradient(135deg,#3d6fd0,#9db8ef 55%,#4a67b8)}
.services-intro{left:364px;top:1703px;width:472px;text-align:center;font-size:13.5px;line-height:19.5px}

.card{width:206px}
.card-img{width:206px;height:141px}
.card h3{margin-top:26px;font-size:11.8px;font-weight:600;color:var(--navy)}
.card p{margin-top:9px;font-size:10.2px;line-height:16.3px}

.divider{left:159px;top:2535px;width:884px;height:2px;background:var(--rule)}
.map{left:258px;top:2685px;width:378px;height:284px;border:1px solid #c9ccd1;background:linear-gradient(160deg,#eef0ec,#e4e8e2 60%,#eceee9)}
.contact{left:683px;top:2682px;font-size:13.8px;line-height:19.4px;color:var(--navy)}
.contact a{color:var(--blue);text-decoration:none}
.footer{left:0;top:3074px;width:1200px;height:51px;background:var(--footer);color:var(--white);font-size:10.5px}
.footer .copy{position:absolute;left:159px;top:18px}
.footer nav{position:absolute;right:159px;top:18px;display:flex;gap:35px}
.footer nav a{color:var(--white);text-decoration:underline}
</style>
</head>
<body>
<div class="page">

  <header>
    <div class="abs hero-bg"></div>
    <div class="abs hero-photo" role="img" aria-label="Hände in weißen Handschuhen halten zwei Gipsmodelle von Kiefern"></div>
    <div class="abs topbar">
      <span><svg width="11" height="11" viewBox="0 0 12 12"><rect x=".5" y=".5" width="11" height="11" rx="2" fill="#4a80c6"/><path d="M3.5 3c.5 2.5 2.5 4.8 5 5.5l.7-1.2-1.4-.8-.6.6c-1-.5-1.8-1.3-2.3-2.3l.6-.6-.8-1.4z" fill="#fff"/></svg>02631 4482</span>
      <span><svg width="12" height="9" viewBox="0 0 12 9"><rect width="12" height="9" rx="1" fill="#4a80c6"/><path d="M0 1l6 4 6-4" stroke="#fff" fill="none"/></svg>info@dentallabor-velmsdorf.de</span>
    </div>
    <div class="abs brand"><i></i>Lindholt</div>
    <h1 class="abs hero-title display">Ihr Partner für Zahntechnik im Raum Velmsdorf bietet Produkte auf höchstem technischem Niveau.</h1>
    <p class="abs hero-text">Lorem ipsum dolor sit amet, consectetuer adipiscing elit. Aenean commodo ligula eget dolor. Aenean massa. Cum sociis natoque penatibus et magnis dis parturient montes, nascetur ridiculus mus.</p>
    <a class="abs btn btn-a">Unsere Leistungen</a>
    <a class="abs btn btn-b">Kontakt</a>
  </header>

  <section class="about">
    <h2 class="abs sec-title display" style="top:764px">Über uns</h2>
    <div class="abs sec-rule" style="top:810px"></div>
    <p class="abs sec-sub" style="top:828px">Dentaltechnik auf technisch höchstem Niveau</p>
    <p class="abs about-text" style="top:872px">Lorem ipsum dolor sit amet, consetetur sadipscing elitr, sed diam nonumy eirmod tempor invidunt ut labore et dolore <b>magna aliquyam erat</b>, sed diam voluptua. At vero eos et accusam et justo duo dolores et ea rebum. Stet clita kasd gubergren, no sea takimata sanctus est Lorem ipsum dolor sit amet. Lorem ipsum dolor sit amet, consetetur sadipscing elitr, sed diam nonumy eirmod tempor invidunt ut labore et dolore magna aliquyam erat, sed diam voluptua. <b>At vero eos et accusam et justo duo dolores</b> et ea rebum. Stet clita kasd gubergren, no sea takimata sanctus est Lorem ipsum dolor sit amet.</p>
    <p class="abs about-text" style="top:1015px">Lorem ipsum dolor sit amet, consetetur sadipscing elitr, sed diam nonumy eirmod tempor invidunt ut labore et dolore magna aliquyam erat, sed diam voluptua. At vero eos et accusam et justo duo dolores et ea rebum. Stet clita kasd gubergren, no sea takimata sanctus est Lorem ipsum dolor sit amet. Lorem ipsum dolor sit amet, consetetur sadipscing elitr.</p>
    <div class="abs photo-lab" role="img" aria-label="Zahntechnikerin arbeitet an einem Gebissmodell im Artikulator"></div>
  </section>

  <section class="services">
    <div class="abs services-bg"></div>
    <div class="abs photo-implant" role="img" aria-label="Transparentes Kiefermodell mit Implantatbrücke in blauem Licht"></div>
    <h2 class="abs sec-title display" style="top:1590px">Unsere Leistungen</h2>
    <div class="abs sec-rule" style="top:1637px"></div>
    <p class="abs sec-sub" style="top:1655px">Innovative Produkte made in Germany</p>
    <p class="abs services-intro">Lorem ipsum dolor sit amet, consectetuer adipiscing elit. Aenean commodo ligula eget dolor. Aenean massa. Cum sociis natoque penatibus et magnis dis parturient montes, nascetur ridiculus mus.</p>

    <article class="abs card" style="left:159px;top:1806px"><div class="card-img" role="img" aria-label="Hände reparieren eine Zahnprothese mit einer Zange" style="background:linear-gradient(135deg,#d8d4cf,#b9a89a 50%,#eceae7)"></div><h3>Reparatur von Zahnersatz</h3><p>Lorem ipsum dolor sit amet, consectetuer adipiscing elit. Aenean commodo ligula eget dolor. Aenean massa. Cum sociis natoque penatibus et magnis dis parturient montes, nascetur ridiculus mus. Lorem ipsum dolor sit amet, consectetuer adipiscing elit.</p></article>
    <article class="abs card" style="left:383px;top:1806px"><div class="card-img" role="img" aria-label="Zahnreihe mit Implantat in einer Zahnlücke" style="background:linear-gradient(180deg,#b8545e,#e9a3a6 45%,#f1dfd8)"></div><h3>Implantologischer Zahnersatz</h3><p>Lorem ipsum dolor sit amet, consectetuer adipiscing elit. Aenean commodo ligula eget dolor. Aenean massa. Cum sociis natoque penatibus et magnis dis parturient montes, nascetur ridiculus mus. Lorem ipsum dolor sit amet, consectetuer adipiscing elit.</p></article>
    <article class="abs card" style="left:609px;top:1806px"><div class="card-img" role="img" aria-label="Computer mit CAD-Software und Dentalscanner" style="background:linear-gradient(135deg,#cfd8e3,#5a6a7e 50%,#e8ebee)"></div><h3>CAD/CAM Vextra</h3><p>Lorem ipsum dolor sit amet, consectetuer adipiscing elit. Aenean commodo ligula eget dolor. Aenean massa. Cum sociis natoque penatibus et magnis dis parturient montes, nascetur ridiculus mus. Lorem ipsum dolor sit amet, consectetuer adipiscing elit.</p></article>
    <article class="abs card" style="left:834px;top:1806px"><div class="card-img" role="img" aria-label="Teilprothese mit Metallgerüst auf rosa Grund" style="background:linear-gradient(135deg,#f4b9df,#c9c6b8 50%,#f0c4e4)"></div><h3>Kombi-Technik</h3><p>Lorem ipsum dolor sit amet, consectetuer adipiscing elit. Aenean commodo ligula eget dolor. Aenean massa. Cum sociis natoque penatibus et magnis dis parturient montes, nascetur ridiculus mus. Lorem ipsum dolor sit amet, consectetuer adipiscing elit.</p></article>

    <article class="abs card" style="left:159px;top:2162px"><div class="card-img" role="img" aria-label="Keramikmodell eines Gebisses wird mit Pinsel bearbeitet" style="background:linear-gradient(135deg,#dcdcdc,#e9d7b9 50%,#d86a3a)"></div><h3>Keramik</h3><p>Lorem ipsum dolor sit amet, consectetuer adipiscing elit. Aenean commodo ligula eget dolor. Aenean massa. Cum sociis natoque penatibus et magnis dis parturient montes, nascetur ridiculus mus. Lorem ipsum dolor sit amet, consectetuer adipiscing elit.</p></article>
    <article class="abs card" style="left:383px;top:2162px"><div class="card-img" role="img" aria-label="Violetter Zahnabdruck in einem Abformlöffel" style="background:linear-gradient(135deg,#e6e6ea,#9a7fb8 50%,#ecebef)"></div><h3>Modellgusstechnik</h3><p>Lorem ipsum dolor sit amet, consectetuer adipiscing elit. Aenean commodo ligula eget dolor. Aenean massa. Cum sociis natoque penatibus et magnis dis parturient montes, nascetur ridiculus mus. Lorem ipsum dolor sit amet, consectetuer adipiscing elit.</p></article>
    <article class="abs card" style="left:609px;top:2162px"><div class="card-img" role="img" aria-label="Lächelnder älterer Mensch mit Zahnprothese" style="background:linear-gradient(135deg,#e8d8cc,#c9a08a 50%,#efe6df)"></div><h3>Prothetik</h3><p>Lorem ipsum dolor sit amet, consectetuer adipiscing elit. Aenean commodo ligula eget dolor. Aenean massa. Cum sociis natoque penatibus et magnis dis parturient montes, nascetur ridiculus mus. Lorem ipsum dolor sit amet, consectetuer adipiscing elit.</p></article>
    <article class="abs card" style="left:834px;top:2162px"><div class="card-img" role="img" aria-label="Goldkronen und Keramikkronen auf hellem Grund" style="background:linear-gradient(135deg,#f4f4f2,#e2cfa3 45%,#f3f1ec)"></div><h3>Verarbeitungen in Hochgold</h3><p>Lorem ipsum dolor sit amet, consectetuer adipiscing elit. Aenean commodo ligula eget dolor. Aenean massa. Cum sociis natoque penatibus et magnis dis parturient montes, nascetur ridiculus mus. Lorem ipsum dolor sit amet, consectetuer adipiscing elit.</p></article>
  </section>

  <div class="abs divider"></div>

  <section class="contact-section">
    <h2 class="abs sec-title display" style="top:2597px">Kontaktieren Sie uns</h2>
    <div class="abs map" role="img" aria-label="Straßenkarte mit Standortmarkierung des Labors"></div>
    <address class="abs contact" style="font-style:normal">
      Lindholt Dentallabor<br>Werkstraße 9<br>48691 Velmsdorf<br><br>
      Tel.: 02631 4482<br>Fax.: 02631 907153<br>Email: <a>info@dentallabor-velmsdorf.de</a><br><br>
      Inhaltlich verantwortlicher: Torben Lindholt
    </address>
  </section>

  <footer class="abs footer">
    <span class="copy">© 2018 Lindholt Dentallabor</span>
    <nav><a>Impressum</a><a>Datenschutz</a></nav>
  </footer>

</div>
</body>
</html>
```